Business card for Financial Technology company

Hello! We'd like to create business cards for 4 members of our company. Our company is a financial technology business that provides funding for businesses. We want to give it a VC (venture captal) look and feel. Clean, fresh and minimal but with a flair of artistry. I'll include some samples of cards we like. It would be great if the back of the card was artistic (see sample files 1 and 2) and the front of the card was the business info. The name of the company is Northbeam Capital.

```html
<!DOCTYPE html>
<html lang="en">
<head>
<meta charset="utf-8">
<title>Northbeam Capital — Business Card</title>
<link rel="stylesheet" href="https://fonts.googleapis.com/css2?family=Jost:wght@400;500;700&display=swap">
<style>
  :root {
    --stage: #2c2c2c;
    --card-white: #ffffff;
    --ink: #1e1e1e;
    --ink-soft: #4a4a4a;
    --icon-green: #2f9c4c;
    --grad-yellow: #f7d91e;
    --grad-orange: #f08a2a;
    --grad-red: #e8465a;
    --grad-pink: #d93a9a;
    --grad-purple: #b02ac9;
    --frame-white: #ffffff;
  }
  * { box-sizing: border-box; margin: 0; padding: 0; }
  html, body {
    width: 1200px; height: 900px; overflow: hidden;
    background: var(--stage);
    font-family: "Jost", sans-serif;
  }
  .stage {
    width: 1200px; height: 900px;
    display: flex; align-items: center; justify-content: center; gap: 72px;
  }
  .card {
    width: 430px; height: 752px;
    position: relative; overflow: hidden;
  }
  /* Front */
  .card-front {
    background: var(--card-white);
    display: flex; flex-direction: column; align-items: center;
    color: var(--ink);
  }
  .brand {
    margin-top: 190px;
    display: flex; align-items: center; gap: 12px;
  }
  .brand-square {
    width: 20px; height: 20px; background: var(--ink); flex: none;
  }
  .brand-name {
    font-size: 30px; font-weight: 500; color: var(--ink); letter-spacing: 0.5px;
    white-space: nowrap;
  }
  .person { margin-top: 58px; text-align: center; }
  .person-name {
    font-size: 25px; font-weight: 700; letter-spacing: 0.5px; text-transform: uppercase;
  }
  .person-role {
    font-size: 17px; font-weight: 400; color: var(--ink-soft); margin-top: -2px;
  }
  .contact { margin-top: 66px; list-style: none; }
  .contact li {
    display: flex; align-items: center; gap: 10px;
    font-size: 18px; color: var(--ink-soft); line-height: 28px;
    white-space: nowrap;
  }
  .contact svg { width: 16px; height: 16px; flex: none; }
  .address {
    margin-top: 60px; text-align: center;
    font-size: 18px; line-height: 26px; color: var(--ink-soft); font-style: normal;
  }
  /* Back */
  .card-back { display: flex; align-items: center; justify-content: center; }
  .back-art {
    position: absolute; inset: 0;
    background: linear-gradient(135deg,
      var(--grad-yellow) 0%, var(--grad-orange) 30%,
      var(--grad-red) 52%, var(--grad-pink) 72%, var(--grad-purple) 100%);
  }
  .back-frame {
    position: relative;
    width: 230px; height: 230px;
    border: 4px solid var(--frame-white);
    display: flex; align-items: center; justify-content: center;
  }
  .back-brand {
    font-size: 32px; font-weight: 500; line-height: 38px;
    color: var(--frame-white); text-align: center;
  }
</style>
</head>
<body>
<main class="stage">
  <section class="card card-front" aria-label="Card front">
    <div class="brand">
      <span class="brand-square"></span>
      <span class="brand-name">Northbeam Capital</span>
    </div>
    <div class="person">
      <h1 class="person-name">Daniel Harwick</h1>
      <p class="person-role">Founder</p>
    </div>
    <ul class="contact">
      <li>
        <svg viewBox="0 0 16 16" aria-hidden="true"><path fill="var(--icon-green)" d="M3.5 1.5l2.3 2.8-1.4 1.6c.9 2 2.3 3.4 4.2 4.3l1.6-1.4 2.8 2.3-1.2 2.4C6.7 13.2 2.8 9.3 1.2 2.7z"/></svg>
        (888) 555-0147
      </li>
      <li>
        <svg viewBox="0 0 16 16" aria-hidden="true"><rect x="1" y="3" width="14" height="10" fill="var(--icon-green)"/><path d="M1.5 3.5L8 9l6.5-5.5" fill="none" stroke="#fff" stroke-width="1.2"/></svg>
        info@northbeamcapital.com
      </li>
      <li>
        <svg viewBox="0 0 16 16" aria-hidden="true" fill="none" stroke="var(--icon-green)" stroke-width="1.2"><circle cx="8" cy="8" r="6.5"/><ellipse cx="8" cy="8" rx="3" ry="6.5"/><path d="M1.5 8h13M2.5 5h11M2.5 11h11"/></svg>
        www.northbeamcapital.com
      </li>
    </ul>
    <address class="address">
      42 Harbor Point Drive, Suite 210<br>
      Fairview, NJ 07022
    </address>
  </section>

  <section class="card card-back" aria-label="Card back">
    <div class="back-art" role="img" aria-label="Faceted triangle mosaic pattern blending yellow, orange, pink and purple"></div>
    <div class="back-frame">
      <span class="back-brand">Northbeam<br>Capital</span>
    </div>
  </section>
</main>
</body>
</html>
```